Stationary for diaper and toy exchange
Nappy Nest Circle, LLC
Stationary for diaper and toy exchange - Children
Creative Brief
Professional
Merra Velstrand
CEO & Founder
P.O. Box 3926 Centreville, VA 20122
merra@nappynestcircle.example
http://www.nappynestcircle.example
Join. Swap. Save.
odeflori odeflori
WOW! All the card designs are wonderful, I'm excited about finalizing a logo. Keep them coming. Thank you.

```html
<!DOCTYPE html>
<html lang="en">
<head>
<meta charset="utf-8">
<title>Nappy Nest Circle – Business Card</title>
<link href="https://fonts.googleapis.com/css2?family=Roboto+Slab:wght@300;400;700&family=Quicksand:wght@400;500&display=swap" rel="stylesheet">
<style>
  :root {
    --stage: #4a4a4a;
    --paper: #f6f6f4;
    --teal: #6cc3b9;
    --coral: #ef8f76;
    --coral-soft: #f3a88f;
    --yellow: #eee733;
    --charcoal: #4d4d4d;
    --ink: #555555;
    --rule: #9a9a9a;
    --white: #ffffff;
  }
  * { box-sizing: border-box; margin: 0; padding: 0; }
  html, body { width: 1200px; height: 904px; overflow: hidden; }
  body { background: var(--stage); position: relative; font-family: "Quicksand", sans-serif; }

  .card { position: absolute; width: 492px; height: 281px; overflow: hidden; }
  .card-front { left: 87px; top: 324px; background: var(--paper); }
  .card-back { left: 616px; top: 324px; background: var(--coral); }

  /* front */
  .brand {
    position: absolute; left: 14px; top: 110px; width: 222px;
    display: flex; align-items: center; justify-content: center; gap: 7px;
    font-family: "Roboto Slab", serif; font-weight: 700; font-size: 19px; color: var(--teal);
    white-space: nowrap;
  }
  .brand-dot { width: 11px; height: 11px; border-radius: 50%; background: var(--teal); flex: none; }
  .divider { position: absolute; left: 246px; top: 63px; width: 1px; height: 142px; background: var(--rule); }
  .details { position: absolute; left: 264px; top: 58px; width: 212px; color: var(--ink); white-space: nowrap; }
  .person-name { font-family: "Roboto Slab", serif; font-weight: 400; font-size: 18px; color: var(--teal); line-height: 22px; }
  .person-title { font-family: "Roboto Slab", serif; font-weight: 300; font-size: 13.5px; color: var(--coral); line-height: 18px; }
  .address { margin-top: 8px; font-size: 13px; line-height: 17px; }
  .contacts { margin-top: 11px; list-style: none; font-size: 12px; line-height: 19px; }
  .contacts li { display: flex; align-items: center; gap: 6px; }
  .contacts svg { width: 13px; height: 11px; flex: none; }

  .color-band { position: absolute; left: 0; bottom: 0; width: 100%; height: 21px; display: flex; gap: 2px; background: var(--white); }
  .color-band span { flex: 1; }
  .band-teal { background: var(--teal); }
  .band-coral { background: var(--coral); }
  .band-yellow { background: var(--yellow); }
  .band-charcoal { background: var(--charcoal); }

  /* back */
  .back-art { position: absolute; left: 128px; top: 86px; width: 238px; height: 102px; border-radius: 50px; background: var(--coral-soft); }
  .tagline {
    position: absolute; left: 0; top: 194px; width: 100%; text-align: center;
    font-family: "Roboto Slab", serif; font-weight: 400; font-size: 20px; color: var(--white);
  }
  .back-url {
    position: absolute; left: 0; top: 228px; width: 100%; text-align: center;
    font-family: "Roboto Slab", serif; font-weight: 300; font-size: 11px; letter-spacing: 0.42em; color: var(--white);
  }
</style>
</head>
<body>
  <section class="card card-front">
    <div class="brand"><span class="brand-dot"></span>Nappy Nest Circle</div>
    <div class="divider"></div>
    <div class="details">
      <p class="person-name">Merra Velstrand</p>
      <p class="person-title">CEO &amp; Founder</p>
      <p class="address">P.O. Box 3926<br>Centreville, VA 20122</p>
      <ul class="contacts">
        <li>
          <svg viewBox="0 0 13 11" aria-hidden="true"><path d="M1 3.5 Q6.5 0 12 3.5 L11 5 L9 4.2 L9 3 Q6.5 2.2 4 3 L4 4.2 L2 5 Z" fill="var(--teal)"/><rect x="3" y="5.5" width="7" height="5" rx="1" fill="var(--teal)"/></svg>
          555.240.1187
        </li>
        <li>
          <svg viewBox="0 0 13 11" aria-hidden="true"><rect x="0.5" y="1.5" width="12" height="8" fill="var(--teal)"/><path d="M0.5 1.5 L6.5 6 L12.5 1.5" fill="none" stroke="var(--paper)" stroke-width="1"/></svg>
          merra@nappynestcircle.example
        </li>
        <li>
          <svg viewBox="0 0 13 11" aria-hidden="true"><g fill="none" stroke="var(--teal)" stroke-width="0.9"><circle cx="6.5" cy="5.5" r="4.8"/><ellipse cx="6.5" cy="5.5" rx="2" ry="4.8"/><path d="M1.7 5.5 H11.3"/></g></svg>
          www.nappynestcircle.example
        </li>
      </ul>
    </div>
    <div class="color-band">
      <span class="band-teal"></span><span class="band-coral"></span><span class="band-yellow"></span><span class="band-charcoal"></span>
    </div>
  </section>

  <section class="card card-back">
    <div class="back-art" role="img" aria-label="White line illustration of two smiling babies"></div>
    <p class="tagline">Swap . Join . Save</p>
    <p class="back-url">www.nappynestcircle.example</p>
  </section>
</body>
</html>
```